R. T. HOLLOWAY, INC. is a US based Investment firm looking for a five-page website design.

Currently, their temporary site is located at: rtholloway.example and they would like to maintain the site design as much as possible.

R. T. HOLLOWAY, INC. sister companies are: Crestway Lodge Investments (c-lodge.example) Benwick Petroleum (benwick-petroleum.example) and RTHF (rth-foundation.example/en)

Attached is a .ZIP file with designs and assets we think will be useful for your proposal… Content for the site is attached on: rtholloway website content.docx Current temp website design is attached as: Coming Soon Website.zip .EPS Logo files attached as: rtholloway logos.zip Sample business card attached as: R T Holloway Business cards.eps Other assets, such as Fonts and background images attached as: Assets.zip

Target Market(s)

Investors

Industry/Entity Type

Investments

Number of Pages Required

5+ page

Requirements
Must have
• Contact Page with a form.

```html
<!DOCTYPE html>
<html lang="en">
<head>
<meta charset="utf-8">
<title>R. T. Holloway, Inc.</title>
<link href="https://fonts.googleapis.com/css2?family=Marcellus&family=Lato:wght@400;700&display=swap" rel="stylesheet">
<style>
:root{
  --gold:#b19a56;
  --gold-dark:#9c8440;
  --gold-light:#c9b57a;
  --navy:#1f2b3d;
  --navy-2:#2a3a52;
  --ink:#2b2b2b;
  --muted:#5a5a5a;
  --white:#ffffff;
  --line:#e6e2d6;
}
*{box-sizing:border-box;margin:0;padding:0}
html,body{width:1200px;height:4501px;overflow:hidden;background:var(--white)}
body{position:relative;font-family:'Lato',sans-serif;color:var(--ink)}
.abs{position:absolute}
.serif{font-family:'Marcellus',serif}

/* header */
.brand{position:absolute;left:107px;top:18px;width:200px;text-align:center}
.brand-mark{width:50px;height:50px;border:2px solid var(--gold);border-radius:50%;margin:0 auto 6px}
.brand-name{font-family:'Marcellus',serif;font-size:29px;color:var(--navy);letter-spacing:1px;white-space:nowrap}
.brand-sub{font-family:'Marcellus',serif;font-size:12px;color:var(--gold);letter-spacing:2px}
.contact-item{position:absolute;top:46px;display:flex;gap:12px;align-items:center}
.contact-ico{width:38px;height:38px;background:var(--navy);border-radius:6px;display:flex;align-items:center;justify-content:center}
.contact-lbl{font-size:13px;color:var(--gold);text-transform:uppercase}
.contact-val{font-size:14px;color:var(--navy)}
.nav{position:absolute;left:0;top:133px;width:1200px;height:56px;background:var(--gold);display:flex;padding-left:107px}
.nav a{color:var(--white);text-decoration:none;font-size:14px;display:flex;align-items:center;justify-content:center;height:56px;border-right:1px solid rgba(255,255,255,.25)}
.nav a.active{background:var(--navy)}

/* hero */
.hero{position:absolute;left:0;top:189px;width:1200px;height:716px;background:radial-gradient(ellipse at 70% 40%,#2d4a6a 0%,#13233a 55%,#0c1726 100%);overflow:hidden}
.hero-photo{position:absolute;left:500px;top:0;width:700px;height:640px;background:linear-gradient(160deg,rgba(60,90,130,.35),rgba(30,120,150,.25) 60%,rgba(10,20,35,0))}
.hero-kicker{position:absolute;left:107px;top:244px;font-family:'Marcellus',serif;font-size:24px;color:var(--white)}
.hero-title{position:absolute;left:107px;top:272px;font-family:'Marcellus',serif;font-size:38px;color:var(--white)}
.hero-text{position:absolute;left:107px;top:332px;width:380px;font-size:14px;line-height:20px;color:#e8e8e8}
.btn{display:inline-flex;align-items:center;gap:18px;background:var(--gold);color:var(--white);font-size:14px;border-radius:8px;padding:0 12px 0 24px;height:46px;text-decoration:none}
.btn .arr{width:24px;height:24px;border-radius:50%;background:var(--navy);display:flex;align-items:center;justify-content:center}
.btn.dark{background:var(--navy)}
.btn.dark .arr{background:var(--gold)}
.hero .btn{position:absolute;left:107px;top:400px;width:148px}
.dots{display:flex;gap:8px}
.dots i{width:10px;height:10px;border-radius:50%;background:var(--gold);display:block}
.dots i.on{background:transparent;border:2px solid var(--gold)}

/* pillars */
.pillar{position:absolute;top:1013px;width:130px;text-align:center}
.pillar span{display:block;font-family:'Marcellus',serif;font-size:19px;color:var(--navy);margin-top:8px}
h2.section{font-family:'Marcellus',serif;font-weight:400;font-size:36px;color:var(--navy);text-align:center;position:absolute;left:0;width:1200px}

/* about */
.about-img{position:absolute;left:107px;top:1300px;width:454px;height:417px;border-radius:26px;background:linear-gradient(135deg,#3a3229 0%,#8a8c8f 45%,#cfd3d8 70%,#6b6157 100%)}
.badge{position:absolute;left:494px;top:1333px;width:105px;height:103px;background:var(--gold);border:3px solid var(--white);color:var(--white);text-align:center;font-family:'Marcellus',serif}
.badge b{display:block;font-weight:400;font-size:44px;line-height:46px;margin-top:4px}
.badge small{display:block;font-size:16px;line-height:16px}
.badge em{display:block;font-style:normal;font-size:11px}
.about-kicker{position:absolute;left:627px;top:1298px;font-size:13px;font-weight:700;color:var(--gold)}
.about-rule{position:absolute;left:627px;top:1328px;width:135px;height:2px;background:var(--gold)}
.about-text{position:absolute;left:627px;top:1342px;width:470px;font-size:13px;line-height:30px;color:var(--muted)}
.about-text p+p{margin-top:30px}

/* investment */
.invest{position:absolute;left:0;top:1850px;width:1200px;height:941px;background:linear-gradient(180deg,#a58c42 0%,#b7a162 60%,#ab9451 100%)}
.invest h2{font-family:'Marcellus',serif;font-weight:400;font-size:38px;color:var(--white);text-align:center;margin-top:56px}
.card{position:absolute;width:311px;height:314px;background:var(--white);border-radius:16px;text-align:center;padding-top:36px}
.card h3{font-family:'Marcellus',serif;font-weight:400;font-size:22px;color:var(--navy);margin-top:10px}
.card p{font-size:12.5px;line-height:18px;color:var(--muted);padding:0 22px;margin-top:8px;height:56px}
.card .go{width:20px;height:20px;border:1.5px solid var(--muted);border-radius:3px;margin:10px auto 0;display:flex;align-items:center;justify-content:center}
.card.dark{background:var(--navy)}
.card.dark h3,.card.dark p{color:var(--white)}
.card.dark .go{border-color:var(--white)}

/* social */
.social-title{position:absolute;left:107px;top:2922px;font-family:'Marcellus',serif;font-size:34px;color:var(--navy)}
.social-rule{position:absolute;left:107px;top:2978px;width:230px;height:2px;background:var(--gold)}
.social-text{position:absolute;left:107px;top:2986px;width:470px;font-size:13px;line-height:30px;color:var(--muted)}
.social-text p+p{margin-top:30px}
.social-text a{color:#3a6ea5;text-decoration:none}
.land-back{position:absolute;left:671px;top:2886px;width:456px;height:415px;border-radius:26px;background:var(--navy-2)}
.land{position:absolute;left:636px;top:2928px;width:456px;height:419px;border-radius:26px;background:linear-gradient(180deg,#4a6a8c 0%,#b39b8a 30%,#6f5a48 55%,#8a6a45 80%,#3b2f26 100%)}

/* testimonials */
.tcard{position:absolute;top:3551px;width:475px;height:274px;border:1px solid var(--line);border-radius:14px}
.avatar{position:absolute;left:28px;top:64px;width:146px;height:146px;border-radius:50%;background:linear-gradient(180deg,#c9ccd1,#6d7480)}
.quote{position:absolute;left:128px;top:62px;width:40px;height:40px;border-radius:50%;background:var(--gold);color:var(--white);font-family:'Marcellus',serif;font-size:30px;text-align:center;line-height:50px}
.tname{position:absolute;left:192px;top:74px;font-family:'Marcellus',serif;font-size:18px;color:var(--navy)}
.trole{position:absolute;left:192px;top:100px;font-size:14px;color:var(--gold);letter-spacing:1px}
.tquote{position:absolute;left:192px;top:128px;width:260px;font-size:13px;line-height:18px;color:var(--muted)}
.tmore{position:absolute;left:192px;top:195px;font-size:13px;color:var(--muted)}

/* footer */
.foot{position:absolute;left:0;top:3940px;width:1200px;height:455px;background:var(--navy)}
.foot-brand{position:absolute;left:107px;top:4080px;width:200px;text-align:center}
.foot-brand .brand-name{color:var(--white)}
.foot-info{position:absolute;left:117px;top:4212px;font-size:11px;color:var(--white);line-height:30px}
.foot-info div{display:flex;gap:16px;align-items:center}
.form-panel{position:absolute;left:414px;top:4014px;width:370px;height:405px;background:var(--gold);border-radius:18px 18px 0 0}
.form-panel h4{font-family:'Marcellus',serif;font-weight:400;font-size:26px;color:var(--white);text-align:center;margin-top:24px}
.form-rule{width:120px;height:2px;background:var(--navy);margin:12px auto 0;position:relative}
.form-rule::after{content:"";position:absolute;left:55px;top:-4px;width:10px;height:10px;border-radius:50%;background:var(--navy)}
.field{position:absolute;left:40px;width:292px;height:36px;background:var(--white);font-size:11px;color:#888;padding:8px 8px}
.form-panel .btn{position:absolute;left:40px;top:352px;height:40px;width:154px}
.quick{position:absolute;left:929px;top:4108px}
.quick h5{font-family:'Marcellus',serif;font-weight:400;font-size:26px;color:var(--white)}
.quick ul{list-style:none;margin-top:18px}
.quick li{font-size:11px;color:var(--white);line-height:30px;padding-left:24px;position:relative}
.quick li::before{content:"→";position:absolute;left:4px;color:var(--white);font-size:11px}
.copy{position:absolute;left:107px;top:4448px;font-size:14px;color:var(--muted)}
.copy b{font-weight:400;color:var(--gold)}
.socials{position:absolute;left:921px;top:4438px;display:flex;gap:8px}
.socials i{width:32px;height:32px;border-radius:50%;border:2px solid var(--gold);display:block}
.socials i.fill{background:var(--gold)}
</style>
</head>
<body>

<header>
  <div class="brand">
    <div class="brand-mark"></div>
    <div class="brand-name">R. T. HOLLOWAY</div>
    <div class="brand-sub">INC.</div>
  </div>
  <div class="contact-item" style="left:731px">
    <div class="contact-ico"><svg width="16" height="16" viewBox="0 0 24 24"><path d="M6 3l4 4-2 3a12 12 0 006 6l3-2 4 4-3 3C10 21 3 14 3 6z" fill="#b19a56"/></svg></div>
    <div><div class="contact-lbl">Call Us</div><div class="contact-val">555 014 7890</div></div>
  </div>
  <div class="contact-item" style="left:893px">
    <div class="contact-ico"><svg width="18" height="14" viewBox="0 0 18 14"><rect x="1" y="1" width="16" height="12" fill="#b19a56"/><path d="M1 1l8 6 8-6" stroke="#1f2b3d" fill="none" stroke-width="1.5"/></svg></div>
    <div><div class="contact-lbl">Email Us</div><div class="contact-val">name@rtholloway.example</div></div>
  </div>
</header>

<nav class="nav">
  <a class="active" style="width:145px">HOME</a>
  <a style="width:180px">ABOUT US</a>
  <a style="width:245px">INVESTMENT AREAS</a>
  <a style="width:260px">SOCIAL RESPONSIBILITY</a>
  <a style="width:263px;border-right:0">CONTACT US</a>
</nav>

<section class="hero">
  <div class="hero-photo" role="img" aria-label="Businessman in a suit holding a tablet with a glowing rising stock chart"></div>
  <div class="hero-kicker">WELCOME TO</div>
  <div class="hero-title">R. T. HOLLOWAY, INC.</div>
  <p class="hero-text">R. T. Holloway, Inc. helps develop into a great nation and, with assertiveness, stamp its footprint worldwide.</p>
  <a class="btn">Read More <span class="arr"><svg width="12" height="12" viewBox="0 0 12 12"><path d="M2 6h8M7 3l3 3-3 3" stroke="#fff" fill="none" stroke-width="1.5"/></svg></span></a>
  <div class="abs" style="left:582px;top:620px;font-size:11px;color:#ccc">02</div>
  <div class="dots abs" style="left:566px;top:652px"><i></i><i class="on"></i><i></i><i></i></div>
  <svg class="abs" style="left:0;top:596px" width="1200" height="120" viewBox="0 0 1200 120">
    <path d="M0 34 C300 30 500 110 720 118 L1200 118 L1200 120 L0 120Z" fill="#b19a56"/>
    <path d="M0 60 C300 55 500 118 720 120 C950 120 1100 80 1200 50 L1200 120 L0 120Z" fill="#fff"/>
  </svg>
</section>

<section class="pillars">
  <div class="pillar" style="left:185px">
    <svg width="100" height="100" viewBox="0 0 100 100" fill="none" stroke="#b19a56" stroke-width="3"><path d="M5 85l25-30 15 15 15-30 35 45"/><path d="M60 40V10l14 6-14 6"/><path d="M28 70l8 6 8-6 8 6"/></svg>
    <span>Mission</span>
  </div>
  <div class="pillar" style="left:398px">
    <svg width="100" height="100" viewBox="0 0 100 100" fill="none" stroke="#b19a56" stroke-width="3"><circle cx="50" cy="48" r="20"/><path d="M42 68h16v12H42zM44 86h12M50 4v10M24 14l6 8M76 14l-6 8M50 58V46l-6-6M50 46l6-6"/></svg>
    <span>Vision</span>
  </div>
  <div class="pillar" style="left:625px">
    <svg width="100" height="100" viewBox="0 0 100 100" fill="none" stroke="#b19a56" stroke-width="3"><path d="M10 40l15-18h50l15 18-40 52z"/><path d="M10 40h80M35 22l-5 18 20 52 20-52-5-18M50 4v10M30 8l4 8M70 8l-4 8"/></svg>
    <span>Values</span>
  </div>
  <div class="pillar" style="left:836px">
    <svg width="100" height="100" viewBox="0 0 100 100" fill="none" stroke="#b19a56" stroke-width="3"><circle cx="50" cy="12" r="6"/><circle cx="25" cy="30" r="6"/><circle cx="75" cy="30" r="6"/><path d="M42 45V24h16v21M17 62V40h16v22M67 62V40h16v22M10 95V62h80v33M35 95V75h30v20"/></svg>
    <span>Leadership</span>
  </div>
</section>

<h2 class="section" style="top:1212px">ABOUT US</h2>
<div class="about-img" role="img" aria-label="Hands holding a tablet showing financial charts beside a cup of coffee"></div>
<div class="badge"><b>11</b><small>YEAR</small><em>EXPERIENCE</em></div>
<div class="about-kicker">BASED IN HOUSTON, TEXAS, R. T. HOLLOWAY, INC.</div>
<div class="about-rule"></div>
<div class="about-text">
  <p>Based in Houston, Texas, R. T. Holloway, Inc. is an investment company, founded in 2010, with the purpose to foster endeavors for socioeconomic development, and create platforms for harnessing the potential of world resources, designed to meet the demands of the emerging markets. R. T. Holloway, Inc. functions as a vehicle that enables investments, with the goal of developing the multiple opportunities available.</p>
  <p>R. T. Holloway, Inc. holds interests in areas of investment that are vital to the international economy: Sectors of Energy, Mining, Industry, Finance and Real Estate.</p>
</div>
<a class="btn abs" style="left:622px;top:1672px;width:148px">Read More <span class="arr"><svg width="12" height="12" viewBox="0 0 12 12"><path d="M2 6h8M7 3l3 3-3 3" stroke="#fff" fill="none" stroke-width="1.5"/></svg></span></a>

<section class="invest">
  <h2>INVESTMENT AREAS</h2>
</section>
<div class="card" style="left:108px;top:1990px">
  <svg width="90" height="90" viewBox="0 0 90 90" fill="none" stroke="#b19a56" stroke-width="2.5"><path d="M5 86h80M20 86V30h24v56M44 86V10h24v76M68 86V40h14v46M26 40h12M26 52h12M26 64h12M50 22h12M50 34h12M50 46h12M50 58h12"/></svg>
  <h3>ENERGY</h3>
  <p>R. T. Holloway, Inc. holds investments both in Exploration &amp; Production, and support field services...</p>
  <div class="go"><svg width="10" height="10" viewBox="0 0 10 10"><path d="M1 5h7M5 2l3 3-3 3" stroke="#5a5a5a" fill="none" stroke-width="1.3"/></svg></div>
</div>
<div class="card dark" style="left:445px;top:1990px">
  <svg width="90" height="90" viewBox="0 0 90 90" fill="none" stroke="#b19a56" stroke-width="2.5"><path d="M10 20c20-12 40-12 55 5M38 15L15 70M5 86h80L70 50 52 66 40 56 20 86"/></svg>
  <h3>MINING</h3>
  <p>R. T. Holloway, Inc. holds interests in the management of operations of diamond mines, With current production..</p>
  <div class="go"><svg width="10" height="10" viewBox="0 0 10 10"><path d="M1 5h7M5 2l3 3-3 3" stroke="#fff" fill="none" stroke-width="1.3"/></svg></div>
</div>
<div class="card" style="left:781px;top:1990px">
  <svg width="90" height="90" viewBox="0 0 90 90" fill="none" stroke="#b19a56" stroke-width="2.5"><path d="M5 86h80M12 86V50h66v36M20 50V34h10v16M40 50V30h10v20M22 66h46M22 76h46"/><circle cx="62" cy="18" r="10"/><circle cx="48" cy="22" r="7"/></svg>
  <h3>INDUSTRY</h3>
  <p>R. T. Holloway, Inc. holds investments in a paint manufacturing plant with two Warehouses in Viana, Luanda and Cabinda</p>
  <div class="go"><svg width="10" height="10" viewBox="0 0 10 10"><path d="M1 5h7M5 2l3 3-3 3" stroke="#5a5a5a" fill="none" stroke-width="1.3"/></svg></div>
</div>
<div class="card" style="left:108px;top:2332px">
  <svg width="90" height="90" viewBox="0 0 90 90" fill="none" stroke="#b19a56" stroke-width="2.5"><path d="M25 20h20l-6 10c14 6 20 24 12 40H12C4 54 10 36 26 30z"/><circle cx="52" cy="66" r="16"/><path d="M56 60h-7v6h6v6h-7M52 56v4M52 72v4"/><path d="M66 50h20v30H66"/></svg>
  <h3>FINANCE</h3>
  <p>R. T. Holloway, Inc. serves as a platform to capture foreign investments. Our target sectors include</p>
  <div class="go"><svg width="10" height="10" viewBox="0 0 10 10"><path d="M1 5h7M5 2l3 3-3 3" stroke="#5a5a5a" fill="none" stroke-width="1.3"/></svg></div>
</div>
<div class="card" style="left:445px;top:2332px">
  <svg width="90" height="90" viewBox="0 0 90 90" fill="none" stroke="#b19a56" stroke-width="2.5"><path d="M45 45L28 28a10 10 0 0117-12 10 10 0 0117 12z"/><path d="M30 28h8l4-6 4 10 4-6h10"/><path d="M5 62h14v20H5M19 66h20l10 4h14l20-12-6 18-26 8H19"/></svg>
  <h3>HEALTHCARE</h3>
  <p>R. T. Holloway, Inc. is committed to develop an investment project in a healthcare unit, with a diversified offer..</p>
  <div class="go"><svg width="10" height="10" viewBox="0 0 10 10"><path d="M1 5h7M5 2l3 3-3 3" stroke="#5a5a5a" fill="none" stroke-width="1.3"/></svg></div>
</div>
<div class="card" style="left:781px;top:2332px">
  <svg width="90" height="90" viewBox="0 0 90 90" fill="none" stroke="#b19a56" stroke-width="2.5"><path d="M5 44L45 6l40 38M14 36v50h62V36M5 86h80M26 78V62h8v16M40 78V54h8v24M54 78V46h8v32M26 58l14-10 10 6 14-14"/></svg>
  <h3>REAL ESTATE</h3>
  <p>R. T. Holloway, Inc. We have in our portfolio the following projects:</p>
  <div class="go"><svg width="10" height="10" viewBox="0 0 10 10"><path d="M1 5h7M5 2l3 3-3 3" stroke="#5a5a5a" fill="none" stroke-width="1.3"/></svg></div>
</div>
<a class="btn dark abs" style="left:526px;top:2685px;width:150px">Read More <span class="arr"><svg width="12" height="12" viewBox="0 0 12 12"><path d="M2 6h8M7 3l3 3-3 3" stroke="#fff" fill="none" stroke-width="1.5"/></svg></span></a>

<section>
  <div class="social-title">Social Responsibility</div>
  <div class="social-rule"></div>
  <div class="social-text">
    <p>Since the commencement of our activity, R. T. Holloway, Inc. contributes to change the quality of life of children and seniors across the world, providing them with support for primary education and basic medical aid, which we believe to be the right of every human being.</p>
    <p>Proportionally to our growth, R. T. Holloway, Inc. aims to extend our contributions to other communities in Africa and the rest of the World, with more donations to charities and other non-profit organizations via the Rowan T. Holloway Foundation <a>(rth-foundation.example/en/)</a></p>
  </div>
  <a class="btn abs" style="left:107px;top:3275px;width:148px">Read More <span class="arr"><svg width="12" height="12" viewBox="0 0 12 12"><path d="M2 6h8M7 3l3 3-3 3" stroke="#fff" fill="none" stroke-width="1.5"/></svg></span></a>
  <div class="land-back"></div>
  <div class="land" role="img" aria-label="Canyon cliffs overlooking a wide valley at sunset"></div>
</section>

<h2 class="section" style="top:3420px">TESTIMONIALS</h2>
<div class="abs" style="left:0;top:3475px;width:1200px;text-align:center;font-size:13px;color:var(--muted)">+2,500 Clients Love Us</div>
<div class="tcard" style="left:107px">
  <div class="avatar" role="img" aria-label="Portrait of a client in a suit"></div>
  <div class="quote">&rdquo;</div>
  <div class="tname">Daniel Whitford</div>
  <div class="trole">Real estate</div>
  <p class="tquote">Lorem Ipsum is simply dummy text of the printing and typesetting standard text ever since the 1500s</p>
  <div class="tmore">Read More ⊕</div>
</div>
<div class="tcard" style="left:615px">
  <div class="avatar" role="img" aria-label="Portrait of a client in a suit"></div>
  <div class="quote">&rdquo;</div>
  <div class="tname">Marcus Bellamy</div>
  <div class="trole">Director</div>
  <p class="tquote">Lorem Ipsum is simply dummy text of the printing and typesetting standard text ever since the 1500s</p>
  <div class="tmore">Read More ⊕</div>
</div>
<div class="dots abs" style="left:576px;top:3873px"><i class="on"></i><i></i><i></i></div>

<footer>
  <svg class="abs" style="left:0;top:3940px" width="1200" height="80" viewBox="0 0 1200 80">
    <path d="M0 80 L0 70 C400 70 700 -10 1200 10 L1200 80Z" fill="#b19a56"/>
  </svg>
  <div class="foot" style="top:3990px;height:405px"></div>
  <svg class="abs" style="left:0;top:3975px" width="1200" height="40" viewBox="0 0 1200 40">
    <path d="M0 40 L0 32 C400 32 700 10 1200 22 L1200 40Z" fill="#1f2b3d"/>
  </svg>
  <div class="foot-brand">
    <div class="brand-mark"></div>
    <div class="brand-name">R. T. HOLLOWAY</div>
    <div class="brand-sub">INC.</div>
  </div>
  <div class="foot-info">
    <div><svg width="12" height="14" viewBox="0 0 12 14"><path d="M6 0a6 6 0 016 6c0 4-6 8-6 8S0 10 0 6a6 6 0 016-6z" fill="#b19a56"/><circle cx="6" cy="6" r="2" fill="#1f2b3d"/></svg>2210 Meridian Ave, 9th Floor</div>
    <div style="padding-left:28px">Houston, Tx 77001</div>
    <div><svg width="12" height="12" viewBox="0 0 24 24"><path d="M6 3l4 4-2 3a12 12 0 006 6l3-2 4 4-3 3C10 21 3 14 3 6z" fill="#b19a56"/></svg>+1 (555) 014 7890</div>
    <div><svg width="14" height="11" viewBox="0 0 18 14"><rect x="1" y="1" width="16" height="12" fill="#b19a56"/><path d="M1 1l8 6 8-6" stroke="#1f2b3d" fill="none" stroke-width="1.5"/></svg>name@rtholloway.example</div>
  </div>
  <form class="form-panel">
    <h4>Get In Touch</h4>
    <div class="form-rule"></div>
    <div class="field" style="top:88px">👤︎ Name</div>
    <div class="field" style="top:132px">☏ Phone</div>
    <div class="field" style="top:176px">✉︎ Email</div>
    <div class="field" style="top:220px;height:92px">◯ Message</div>
    <a class="btn dark">Read More <span class="arr"><svg width="12" height="12" viewBox="0 0 12 12"><path d="M2 6h8M7 3l3 3-3 3" stroke="#fff" fill="none" stroke-width="1.5"/></svg></span></a>
  </form>
  <div class="quick">
    <h5>Quick Link</h5>
    <ul>
      <li>HOME</li><li>ABOUT US</li><li>INVESTMENT AREAS</li><li>SOCIAL RESPONSIBILITY</li><li>CONTACT US</li>
    </ul>
  </div>
  <div class="copy">Copyright © 2021 <b>R.T HOLLOWAY INC</b>, All Rights Reserved.</div>
  <div class="socials"><i class="fill"></i><i></i><i></i><i></i></div>
</footer>

</body>
</html>
```